Business card design for new eCommerce site focusing on integrity and strong businsess tactics

We need a business card that will stand out and be memorable. Something with color that matches our company logo colors. Think high end version of Dealvine. There are 2 logos provided. The parent company is called Bright Harbor Ventures and we are presenting a new and very exciting eCommerce site called KeenTraders.example.

Target Market(s)

Our target markets are in the Activities, Food and Beverage, Health and Beauty

Industry/Entity Type

Marketing

Contact Information for Business Card

We have 4 members that need cards...I will provide all info to the winner of the design contest
Business Address is
48730 West 61st Avenue, Suite C204
Phoenix AZ 85917

Font styles to use
Serif
Sans Serif

Colors

Designer to choose colors to be used in the design.

Requirements
Must have
• The card must be memorable...should be unique in design but must exude integrity and be playful .
• I have provided several colors or our parent company...please feel free to use which ever
Nice to have
• I will leave this up to you. Feel free to use other images of your choosing that wraps around our client.....Activities, Dining, Health, Beauty
Should not have
• just dont be boring

```html
<!DOCTYPE html>
<html lang="en">
<head>
<meta charset="utf-8">
<title>KeenTraders.example business card</title>
<link rel="stylesheet" href="https://fonts.googleapis.com/css2?family=Quicksand:wght@400;600;700&family=Open+Sans:wght@400;600&display=swap">
<style>
  :root {
    --green: #6cb33f;
    --green-dark: #4f9a2a;
    --lime: #b9d65a;
    --blue: #3a9ad1;
    --grey-text: #666a6d;
    --card-white: #ffffff;
    --card-shade: #eceeec;
    --page: #e9e6e1;
  }
  * { box-sizing: border-box; margin: 0; padding: 0; }
  html, body { width: 1200px; height: 1023px; overflow: hidden; }
  body {
    background: var(--page);
    font-family: "Open Sans", sans-serif;
    position: relative;
  }
  .card {
    position: absolute;
    width: 560px;
    height: 320px;
    border-radius: 16px;
    overflow: hidden;
    background: linear-gradient(160deg, var(--card-white) 45%, var(--card-shade));
    box-shadow: 0 10px 28px rgba(0,0,0,.18);
  }
  .card--front { left: 320px; top: 150px; }
  .card--back { left: 320px; top: 540px; }

  .band {
    position: absolute;
    left: 0; right: 0; bottom: 0;
    height: 38px;
    background: linear-gradient(180deg, var(--green), var(--green-dark));
    color: #fff;
    font-size: 12px;
    display: flex; align-items: center; justify-content: center;
    letter-spacing: .3px;
  }

  /* front */
  .brand {
    position: absolute; left: 34px; top: 40px;
    display: flex; align-items: center; gap: 12px;
  }
  .brand__dot {
    width: 22px; height: 22px; border-radius: 50%;
    background: var(--blue);
  }
  .brand__name {
    font-family: "Quicksand", sans-serif; font-weight: 700;
    font-size: 28px; color: var(--green); letter-spacing: -.3px;
  }
  .brand__tagline {
    position: absolute; left: 68px; top: 80px;
    font-size: 11.5px; color: var(--grey-text); letter-spacing: .4px;
  }
  .holder {
    position: absolute; right: 30px; top: 118px;
    font-family: "Quicksand", sans-serif; font-size: 22px;
    color: var(--blue); letter-spacing: 2px;
  }
  .divider { position: absolute; left: 0; top: 0; }
  .contact {
    position: absolute; left: 34px; top: 196px;
    list-style: none; font-size: 11.5px; color: var(--blue); line-height: 22px;
  }
  .contact li { display: flex; align-items: center; gap: 8px; }
  .contact svg { width: 11px; height: 11px; }
  .address {
    position: absolute; right: 30px; top: 168px;
    font-size: 11.5px; color: var(--blue); line-height: 18px; text-align: right;
    display: flex; gap: 8px; align-items: flex-start;
  }
  .address svg { width: 11px; height: 14px; margin-top: 2px; }

  /* back */
  .mark {
    position: absolute; left: 0; right: 0; top: 0; bottom: 38px;
    display: flex; align-items: center; justify-content: center; gap: 26px;
  }
  .mark__circle {
    width: 120px; height: 120px; border-radius: 50%;
    background: var(--lime);
    box-shadow: 0 0 0 5px #fff, 0 0 0 7px var(--lime);
  }
  .mark__name {
    font-family: "Quicksand", sans-serif; font-weight: 700;
    font-size: 34px; color: var(--lime); line-height: 1.1;
  }
</style>
</head>
<body>

<section class="card card--front" aria-label="Card front">
  <svg class="divider" width="560" height="320" aria-hidden="true">
    <polyline points="530,154 320,154 270,282" fill="none" stroke="var(--green)" stroke-width="1"/>
  </svg>
  <div class="brand">
    <span class="brand__dot"></span>
    <span class="brand__name">KeenTraders.example</span>
  </div>
  <p class="brand__tagline">Deals-Events-Wellness-Style</p>
  <p class="holder">Your Name</p>
  <ul class="contact">
    <li><svg viewBox="0 0 12 12"><path d="M2 1l2 0 1 3-1.5 1a7 7 0 0 0 3.5 3.5L8 7l3 1v2l-1 1A9 9 0 0 1 1 2z" fill="var(--green)"/></svg>88 555 70412</li>
    <li><svg viewBox="0 0 12 12"><rect x="1.5" y="1.5" width="9" height="9" fill="none" stroke="var(--green)"/></svg>88 555 31908</li>
    <li><svg viewBox="0 0 12 12"><rect x="1" y="2.5" width="10" height="7" fill="var(--green)"/><path d="M1 2.5l5 4 5-4" fill="none" stroke="#fff"/></svg>hello@keentraders.example</li>
  </ul>
  <div class="address">
    <p>48730 West 61st Avenue<br>Suite C204, Phoenix AZ 85917</p>
    <svg viewBox="0 0 12 16"><path d="M6 1a5 5 0 0 1 5 5c0 4-5 9-5 9S1 10 1 6a5 5 0 0 1 5-5z" fill="var(--green)"/><circle cx="6" cy="6" r="2" fill="#fff"/></svg>
  </div>
  <div class="band">www.keentraders.example</div>
</section>

<section class="card card--back" aria-label="Card back">
  <div class="mark">
    <span class="mark__circle"></span>
    <p class="mark__name">Bright Harbor<br>Ventures</p>
  </div>
  <div class="band"></div>
</section>

</body>
</html>
```